Redesign the *Settings* screen for the PelikoZ app.

PelikoZ app is in production, but we need to refresh and redesign the settings screen to be cleaner, easier, more intuitive, and more professional looking.

Project Deadline Extended
Reason: Several designers have requested more time. This will also give time to provide feedback on existing designs.

Requirements
Must have
• Black background, so that the screen is consistent with the rest of the app.

```html
<!DOCTYPE html>
<html lang="en">
<head>
<meta charset="utf-8">
<title>PelikoZ – Settings</title>
<link rel="stylesheet" href="https://fonts.googleapis.com/css2?family=Montserrat:wght@400;600;700&family=Russo+One&display=swap">
<style>
  :root {
    --stage: #8d0019;
    --screen: #101112;
    --screen-light: #2a2b2d;
    --tile: #e9eef1;
    --ink: #111;
    --accent: #29e3dc;
    --accent-glow: rgba(41, 227, 220, 0.75);
    --label: #e9e9e9;
    --muted: #9a9a9a;
  }
  * { box-sizing: border-box; margin: 0; padding: 0; }
  html, body { width: 1200px; height: 901px; overflow: hidden; }
  body {
    background: var(--stage);
    font-family: "Montserrat", sans-serif;
    display: flex; align-items: center; justify-content: center;
  }
  .settings-screen {
    width: 480px; height: 852px;
    background: radial-gradient(circle at 60% 50%, var(--screen-light), var(--screen) 70%);
    position: relative; overflow: hidden;
    color: var(--label);
  }
  .status-bar {
    height: 26px; padding: 0 14px;
    display: flex; align-items: center; justify-content: space-between;
    font-size: 12px; color: var(--muted);
  }
  .status-bar .signal { display: flex; gap: 3px; align-items: center; }
  .status-bar .signal i { width: 6px; height: 6px; border-radius: 50%; background: var(--muted); display: block; }
  .status-bar .battery { display: flex; align-items: center; gap: 6px; }
  .battery-cell { width: 26px; height: 11px; border: 1px solid var(--muted); border-radius: 2px; padding: 1px; }
  .battery-cell span { display: block; height: 100%; background: var(--muted); }
  .section-title {
    font-size: 19px; font-weight: 600; letter-spacing: 0.5px;
    text-align: center; margin: 18px 0 14px;
  }
  .tile-row { display: flex; gap: 18px; padding: 0 24px; }
  .tile-row.scroll { overflow: hidden; padding-right: 0; }
  .option-tile {
    flex: 0 0 auto; width: 140px; height: 112px;
    background: var(--tile); border-radius: 12px;
    display: flex; flex-direction: column; align-items: center; justify-content: center; gap: 10px;
    color: var(--ink);
    font-family: "Russo One", sans-serif; font-size: 14px; text-transform: uppercase;
  }
  .option-tile.is-active {
    background: #dffcfb; color: var(--accent);
    box-shadow: 0 0 22px 6px var(--accent-glow);
  }
  .option-tile.large { width: 170px; height: 140px; }
  .tile-art { width: 90px; height: 44px; border-radius: 6px; background: #2b2d30; }
  .is-active .tile-art { background: var(--accent); }
  .tile-art.hand { width: 54px; height: 58px; border-radius: 24px 24px 14px 14px; }
  .tile-art.round { width: 22px; height: 62px; border-radius: 11px 11px 3px 3px; }
  .tile-art.mag { width: 28px; height: 58px; border-radius: 3px; }
  .co2 { font-family: "Russo One", sans-serif; font-size: 38px; color: var(--ink); }
  .co2 sub { font-size: 18px; }
  .firearm-field {
    margin: 0 24px; display: flex; align-items: flex-end; justify-content: space-between;
    border-bottom: 1px solid var(--accent); padding-bottom: 8px;
  }
  .firearm-field .value { font-family: "Russo One", sans-serif; font-size: 22px; color: var(--accent); }
  .tab-bar {
    position: absolute; left: 0; right: 0; bottom: 0; height: 74px;
    background: #0a0a0a; display: flex;
  }
  .tab { flex: 1; display: flex; flex-direction: column; align-items: center; justify-content: center; gap: 6px; font-size: 13px; color: var(--label); }
  .tab.is-current { color: var(--accent); }
  .tab svg { width: 24px; height: 24px; }
</style>
</head>
<body>
<main class="settings-screen">
  <div class="status-bar">
    <div class="signal"><i></i><i></i><i></i><i></i><span>&nbsp;FFF</span></div>
    <div class="battery">100% <div class="battery-cell"><span></span></div></div>
  </div>

  <h2 class="section-title">Firearms</h2>
  <div class="tile-row scroll">
    <div class="option-tile is-active"><div class="tile-art" role="img" aria-label="Pistol outline"></div>Pistols</div>
    <div class="option-tile"><div class="tile-art" role="img" aria-label="Rifle outline"></div>Rifles</div>
    <div class="option-tile"><div class="tile-art" role="img" aria-label="Shotgun outline"></div>Shotguns</div>
  </div>

  <h2 class="section-title">Current Firearm</h2>
  <div class="firearm-field">
    <span class="value">K240</span>
    <svg width="22" height="22" viewBox="0 0 22 22" fill="none" stroke="#e9e9e9" stroke-width="2"><circle cx="9" cy="9" r="7"/><line x1="14" y1="14" x2="20" y2="20"/></svg>
  </div>

  <h2 class="section-title">Charging handle</h2>
  <div class="tile-row" style="justify-content:center">
    <div class="option-tile large"><div class="tile-art hand" role="img" aria-label="Left hand pointing"></div>Left Hand</div>
    <div class="option-tile large is-active"><div class="tile-art hand" role="img" aria-label="Right hand pointing"></div>Right Hand</div>
  </div>

  <h2 class="section-title">Dry Practice</h2>
  <div class="tile-row" style="gap:14px;padding:0 22px">
    <div class="option-tile is-active"><div class="tile-art round" role="img" aria-label="Cartridge"></div></div>
    <div class="option-tile"><div class="tile-art mag" role="img" aria-label="Magazine"></div></div>
    <div class="option-tile"><span class="co2">CO<sub>2</sub></span></div>
  </div>

  <nav class="tab-bar">
    <div class="tab"><svg viewBox="0 0 24 24" fill="none" stroke="currentColor" stroke-width="2"><circle cx="12" cy="12" r="8"/><path d="M12 1v6M12 17v6M1 12h6M17 12h6"/></svg>Train</div>
    <div class="tab"><svg viewBox="0 0 24 24" fill="none" stroke="currentColor" stroke-width="2"><path d="M20 12a8 8 0 1 1-3-6.2"/><path d="M18 2v5h-5"/></svg>History</div>
    <div class="tab"><svg viewBox="0 0 24 24" fill="currentColor"><path d="M12 3l10 5-10 5L2 8z"/><path d="M4 12l8 4 8-4v3l-8 4-8-4z"/></svg>Learning</div>
    <div class="tab is-current"><svg viewBox="0 0 24 24" fill="none" stroke="currentColor" stroke-width="2"><path d="M3 6h18M3 12h18M3 18h18"/><path d="M8 3v6M16 9v6M10 15v6"/></svg>Settings</div>
  </nav>
</main>
</body>
</html>
```